Welding company needs a business card

We are looking for a logo and business card.

Contact Information for Business Card

418 Cobblestone Lane
Millbrook, PA 17415
410-555-0173
Rmfabworksco@quorvamail.com

```html
<!DOCTYPE html>
<html lang="en">
<head>
<meta charset="utf-8">
<title>RM Fabworks Co — Business Card</title>
<link rel="stylesheet" href="https://fonts.googleapis.com/css2?family=Saira:wdth,wght@110,400;110,700;110,800&display=swap">
<style>
  :root {
    --backdrop: #8a8a8a;
    --card-black: #0b0b0b;
    --brand-red: #ec1c24;
    --ink-white: #ffffff;
    --steel-light: #cfcfcf;
    --steel-dark: #4a4a4a;
  }
  * { box-sizing: border-box; margin: 0; padding: 0; }
  html, body {
    width: 1200px; height: 884px; overflow: hidden;
    background: var(--backdrop);
    font-family: "Saira", sans-serif;
    font-stretch: 110%;
  }
  .canvas {
    position: relative; width: 1200px; height: 884px;
    display: flex; align-items: center; justify-content: center;
  }
  .business-card {
    position: relative; width: 1050px; height: 600px;
    background: var(--card-black); color: var(--ink-white);
    overflow: hidden;
  }
  .brand-block {
    position: absolute; left: 60px; top: 100px; width: 440px; height: 330px;
  }
  .welder-illustration {
    position: absolute; left: 200px; top: 0; width: 220px; height: 220px;
    border-radius: 8px;
    background: linear-gradient(160deg, var(--steel-light), var(--steel-dark));
  }
  .brand-name {
    position: absolute; left: 0; top: 236px;
    display: flex; align-items: center; gap: 12px;
    font-weight: 800; font-size: 38px; letter-spacing: -0.5px;
    color: var(--ink-white); white-space: nowrap;
  }
  .brand-mark {
    width: 28px; height: 28px; background: var(--brand-red); flex: none;
  }
  .name-band {
    position: absolute; left: 530px; top: 148px; width: 520px; height: 112px;
    background: var(--brand-red);
    clip-path: polygon(0 0, 100% 0, 100% 100%, 3% 100%);
    padding: 14px 0 0 38px;
  }
  .person-name { font-weight: 700; font-size: 36px; line-height: 1.1; letter-spacing: 1px; }
  .person-title { font-weight: 400; font-size: 25px; line-height: 1.2; letter-spacing: 1px; }
  .contact-list {
    position: absolute; left: 548px; top: 290px;
    list-style: none; font-size: 26px; font-weight: 400; letter-spacing: 1px; line-height: 1.3;
  }
  .contact-list li { display: flex; align-items: center; gap: 12px; white-space: nowrap; }
  .contact-list .address-line { padding-left: 6px; }
  .contact-list .phone { margin-top: 14px; }
  .contact-icon { width: 22px; height: 22px; flex: none; }
</style>
</head>
<body>
<main class="canvas">
  <section class="business-card">
    <div class="brand-block">
      <div class="welder-illustration" role="img" aria-label="Illustration of a welder in a helmet working with a torch and sparks"></div>
      <div class="brand-name"><span class="brand-mark"></span>RM FABWORKS CO</div>
    </div>

    <div class="name-band">
      <p class="person-name">Daniel Whitaker</p>
      <p class="person-title">Founder</p>
    </div>

    <ul class="contact-list">
      <li class="address-line">418 Cobblestone Lane</li>
      <li class="address-line">Millbrook, PA 17415</li>
      <li class="phone">
        <svg class="contact-icon" viewBox="0 0 24 24" aria-hidden="true">
          <path fill="var(--brand-red)" d="M6.6 10.8c1.4 2.8 3.8 5.1 6.6 6.6l2.2-2.2c.3-.3.7-.4 1-.2 1.1.4 2.3.6 3.6.6.6 0 1 .4 1 1V20c0 .6-.4 1-1 1C10.6 21 3 13.4 3 4c0-.6.4-1 1-1h3.5c.6 0 1 .4 1 1 0 1.3.2 2.5.6 3.6.1.3 0 .7-.2 1z"/>
        </svg>
        410-555-0173
      </li>
      <li class="email">
        <svg class="contact-icon" viewBox="0 0 24 24" aria-hidden="true">
          <rect x="2.5" y="5" width="19" height="14" fill="none" stroke="var(--brand-red)" stroke-width="2"/>
          <path d="M2.5 5l9.5 8 9.5-8M2.5 19l7-6.5M21.5 19l-7-6.5" fill="none" stroke="var(--brand-red)" stroke-width="2"/>
        </svg>
        Rmfabworksco@quorvamail.com
      </li>
    </ul>
  </section>
</main>
</body>
</html>
```